New label for maple syrup business

We are Vindra Farm, a small but mighty maple syrup operation from Quebec, Canada. We sell our syrup in glass bottles and while we have a sharp label, we would like to tweak it. "Vindra" is a nod to our Swedish background, it is the verb 'to love, adore, cherish' We would like our new label to maintain a heart image(can be a different heart! We like the 'drawn' look of the one from our site)
We would like the label to be youthful, textured, warm and definitely not traditional!
Please see attached existing labels (for our four bottle types) and website (vindrafarm.ca) to get an idea of our existing company image.
The size of the label should remain the same- 2.75" high and 7.5" wide.
Please feel free to change the font, background colour and layout
We look forward to your creativity!
Updates

Reason: We would like to see some more submissions from other designers. Thank you!

Industry/Entity Type

Business

Requirements
Must have
• Farm name: Vindra Farm (not La ferme vindra as is currently on the label)
See attached file, maintain existing information on the four labels. Eliminate the establishment number(8147)
Nutritional information still on label but can be presented differently i.e. not in traditional box

```html
<!DOCTYPE html>
<html lang="en">
<head>
<meta charset="utf-8">
<title>Vindra Farm – natural maple syrup label</title>
<link href="https://fonts.googleapis.com/css2?family=Exo+2:wght@500;600;700&display=swap" rel="stylesheet">
<style>
  :root {
    --label-orange: #f05a33;
    --texture-orange: #d9482a;
    --ink: #1a1410;
    --title-red: #d8283a;
    --heart-red: #d42a3c;
    --art-purple: #5b3f86;
    --art-cream: #fbeee6;
  }
  * { margin: 0; padding: 0; box-sizing: border-box; }
  html, body { width: 1200px; height: 440px; overflow: hidden; background: var(--label-orange); }
  .label {
    position: relative; width: 1200px; height: 440px; overflow: hidden;
    background: var(--label-orange); color: var(--ink);
    font-family: "Exo 2", sans-serif; font-weight: 600;
  }
  .texture { position: absolute; top: 0; left: 0; width: 1200px; height: 440px; }
  .contact { position: absolute; left: 20px; top: 6px; width: 380px; text-align: center; font-size: 13.5px; line-height: 16.5px; }
  .nutrition { position: absolute; left: 20px; top: 96px; width: 380px; text-align: center; }
  .nutrition .heading { font-size: 14px; line-height: 16.5px; }
  .nutrition .rows { margin-top: 2px; font-size: 9.6px; line-height: 12.8px; }
  .care { position: absolute; left: 20px; top: 386px; width: 380px; text-align: center; font-size: 13.5px; line-height: 16px; }
  .farm-name {
    position: absolute; left: 405px; top: 34px; white-space: nowrap;
    font-size: 60px; line-height: 72px; font-weight: 700; color: var(--title-red); letter-spacing: 1px;
  }
  .pour-art { position: absolute; left: 595px; top: 112px; width: 205px; height: 256px; }
  .glass-heart { position: absolute; left: 632px; top: 258px; width: 58px; height: 52px; }
  .product-en, .product-fr { position: absolute; font-size: 17px; line-height: 20px; white-space: nowrap; }
  .product-en { left: 405px; top: 222px; transform: rotate(48deg); transform-origin: left center; }
  .product-fr { left: 664px; top: 364px; transform: rotate(-61deg); transform-origin: left center; }
  .grade { position: absolute; top: 412px; font-size: 19px; }
  .grade.class { left: 432px; }
  .grade.volume { left: 587px; }
  .story { position: absolute; left: 880px; top: 10px; width: 292px; font-size: 15.2px; line-height: 19.6px; }
  .story p + p { margin-top: 19px; }
</style>
</head>
<body>
<main class="label">
  <svg class="texture" viewBox="0 0 1200 440" role="img" aria-label="Scribbled hand-drawn heart texture behind the side text panels">
    <defs>
      <radialGradient id="texture-left" cx="0.5" cy="0.5" r="0.5">
        <stop offset="0" stop-color="var(--texture-orange)" stop-opacity="0.7"/>
        <stop offset="1" stop-color="var(--texture-orange)" stop-opacity="0"/>
      </radialGradient>
    </defs>
    <ellipse cx="210" cy="250" rx="200" ry="160" fill="url(#texture-left)"/>
    <ellipse cx="1020" cy="230" rx="200" ry="170" fill="url(#texture-left)"/>
  </svg>

  <section class="contact">
    <p>27 rang des Érables, Lacroix, Québec, J0B 2K0</p>
    <p>lacroix and bellerive, qc</p>
    <p>819.555.0172</p>
    <p>vindra7@mailbox.ca</p>
  </section>

  <section class="nutrition">
    <div class="heading">
      <p>Valeur nutritive</p>
      <p>Nutrition Facts</p>
      <p>par 1/4 tasse (60 mL)</p>
      <p>Per 1/4 cup (60 mL)</p>
    </div>
    <div class="rows">
      <p>Teneur % de valeur quotidienne</p>
      <p>Amount &nbsp;&nbsp;&nbsp;&nbsp; % Daily Value</p>
      <p>Calories / Calories 220</p>
      <p>Lipides / Fat 0 g &nbsp;&nbsp;&nbsp; 0 %</p>
      <p>Sodium / Sodium 10 mg &nbsp;&nbsp; 0 %</p>
      <p>Potassium / Potassium 180 mg &nbsp; 5 %</p>
      <p>Glucides / Carbohydrate 54 mg 18 %</p>
      <p>Sucres / Sugars 48 g</p>
      <p>Protéines / Protein 0 g</p>
      <p>Calcium / Calcium &nbsp;&nbsp;&nbsp; 4 %</p>
      <p>Riboflavine / Riboflavin &nbsp;&nbsp;&nbsp;&nbsp; 25 %</p>
      <p>Magnésium / Magnesium &nbsp;&nbsp;&nbsp; 4 %</p>
      <p>Zinc / Zinc &nbsp;&nbsp;&nbsp;&nbsp;&nbsp;&nbsp;&nbsp; 4 %</p>
      <p>Source négligeable de saturés, trans, cholestérol,</p>
      <p>fibres, vitamine A, vitamine C et fer</p>
      <p>Not a significant source of saturated, trans,</p>
      <p>cholesterol, fibre, vitamin A, vitamin C or iron</p>
    </div>
  </section>

  <section class="care">
    <p>Please recycle this bottle</p>
    <p>Veuillez recycler cette bouteille</p>
    <p>Refrigerate after opening / Réfrigérer une fois ouvert</p>
  </section>

  <h1 class="farm-name">Vindra Farm</h1>

  <svg class="pour-art" viewBox="0 0 205 256" role="img" aria-label="Illustration of a bottle pouring a drop of maple syrup into a glass">
    <defs>
      <linearGradient id="pour-tone" x1="0" y1="0" x2="0" y2="1">
        <stop offset="0" stop-color="var(--art-purple)"/>
        <stop offset="0.45" stop-color="#c9b4d6"/>
        <stop offset="1" stop-color="var(--art-cream)"/>
      </linearGradient>
    </defs>
    <rect x="0" y="0" width="205" height="256" rx="14" fill="url(#pour-tone)" opacity="0.6"/>
  </svg>

  <svg class="glass-heart" viewBox="0 0 58 52" aria-hidden="true">
    <path d="M29 50 C10 36 2 26 2 15 C2 7 8 2 15 2 C21 2 26 6 29 11 C32 6 37 2 43 2 C50 2 56 7 56 15 C56 26 48 36 29 50 Z" fill="var(--heart-red)"/>
  </svg>

  <p class="product-en">natural maple syrup</p>
  <p class="product-fr">sirop d'érable naturel</p>

  <p class="grade class">Canada No. 1</p>
  <p class="grade volume">light / clair 946 mL</p>

  <section class="story">
    <p>vindra: swedish (v): to love, adore, be fond of, cherish<br>
    This natural maple syrup originates from our family farm in the heart of the Eastern Townships of Québec. Every spring we harvest forty litres of clear sap from each maple tree to produce one golden litre of syrup. Nothing is added but love! Enjoy!</p>
    <p>vindra: (v) suédois: aimer, adorer, chérir<br>
    Ce sirop d'érable, entièrement naturel, provient de notre ferme familiale située dans les Cantons de l'Est du Québec. À tous les printemps, nous récoltons de chaque arbre quarante litres d'eau d'érable, que nous transformons en un litre de sirop doré. Rien n'est ajouté, sauf de l'amour! Bon appétit!</p>
  </section>
</main>
</body>
</html>
```